Stationery International Trade Company
Coral Vantage Ltd
Stationery International Trade Company - Trade
Creative Brief
Simple
Milo Harrigan
Sales Director
Latchford St, Bromley
Milo.harrigan@coralvantage.com
www.coralvantage.com
We want the tagline on all stationery "Global Stock Solutions"

```html
<!DOCTYPE html>
<html lang="en">
<head>
<meta charset="utf-8">
<title>Coral Vantage Ltd — Stationery</title>
<link rel="stylesheet" href="https://fonts.googleapis.com/css2?family=Montserrat:wght@400;600;700&display=swap">
<style>
  :root {
    --backdrop: #e6e3df;
    --paper: #ffffff;
    --charcoal: #3a3a3c;
    --coal: #2b2b2d;
    --ember: #f05a22;
    --flame: #f7941d;
    --crimson: #d7261e;
    --ink: #4a4a4a;
    --mute: #9a9a9a;
    --label: #6d6760;
  }
  html, body { margin: 0; padding: 0; overflow: hidden; }
  body { width: 1200px; height: 466px; background: var(--backdrop); font-family: "Montserrat", sans-serif; }
  .stationery-set { position: relative; width: 1200px; height: 466px; }
  .stationery-set svg { position: absolute; display: block; }
  .set-title { position: absolute; left: 15px; top: 138px; font-size: 6px; letter-spacing: 0.8px; color: var(--label); text-transform: uppercase; }
  .piece-label { font-family: "Montserrat", sans-serif; font-size: 6px; letter-spacing: 0.8px; fill: var(--label); text-transform: uppercase; }
  .brand-name { font-family: "Montserrat", sans-serif; font-weight: 700; fill: var(--ember); }
  .tagline { font-family: "Montserrat", sans-serif; font-weight: 400; fill: var(--mute); letter-spacing: 0.6px; }
  .contact-text { font-family: "Montserrat", sans-serif; font-size: 5px; fill: var(--ink); }
  .contact-light { font-family: "Montserrat", sans-serif; font-size: 5px; fill: #dddddd; }
</style>
</head>
<body>
<main class="stationery-set">

  <div class="set-title">Stationery · Coral Vantage</div>

  <!-- Business card front -->
  <svg class="business-card-front" style="left:15px;top:155px" width="100" height="72" viewBox="0 0 100 72">
    <rect width="100" height="58" fill="var(--paper)"/>
    <path d="M0 44 Q40 36 100 50 L100 58 L0 58 Z" fill="var(--ember)"/>
    <path d="M0 50 Q45 44 100 56 L100 58 L0 58 Z" fill="var(--charcoal)"/>
    <circle cx="12" cy="14" r="4" fill="var(--ember)"/>
    <text class="brand-name" x="19" y="16" font-size="6">CORAL VANTAGE LTD</text>
    <text class="tagline" x="19" y="21" font-size="3">GLOBAL STOCK SOLUTIONS</text>
    <text class="contact-text" x="52" y="30" font-size="4" style="font-size:4px;font-weight:600">Milo Harrigan</text>
    <text class="contact-text" x="52" y="34" style="font-size:3px">Sales Director</text>
    <text class="piece-label" x="0" y="68">Business Card Front</text>
  </svg>

  <!-- Business card back -->
  <svg class="business-card-back" style="left:15px;top:232px" width="100" height="72" viewBox="0 0 100 72">
    <rect width="100" height="58" fill="var(--coal)"/>
    <path d="M0 46 Q45 38 100 50 L100 58 L0 58 Z" fill="var(--ember)"/>
    <circle cx="30" cy="24" r="4" fill="var(--ember)"/>
    <text class="brand-name" x="37" y="26" font-size="6">CORAL VANTAGE</text>
    <text class="piece-label" x="0" y="68">Business Card Back</text>
  </svg>

  <!-- Letterhead option 1 -->
  <svg class="letterhead-option-one" style="left:150px;top:12px" width="305" height="450" viewBox="0 0 305 450">
    <rect width="305" height="432" fill="var(--paper)"/>
    <circle cx="22" cy="30" r="7" fill="var(--ember)"/>
    <text class="brand-name" x="34" y="30" font-size="10">CORAL VANTAGE LTD</text>
    <text class="tagline" x="34" y="37" font-size="4.5">GLOBAL STOCK SOLUTIONS</text>
    <g class="contact-block">
      <rect x="195" y="17" width="4" height="4" fill="var(--ember)"/>
      <text class="contact-text" x="203" y="21">+44 20 7946 0321</text>
      <rect x="195" y="25" width="4" height="4" fill="var(--ember)"/>
      <text class="contact-text" x="203" y="29">Milo.harrigan@coralvantage.com</text>
      <rect x="195" y="33" width="4" height="4" fill="var(--ember)"/>
      <text class="contact-text" x="203" y="37">www.coralvantage.com</text>
      <rect x="195" y="41" width="4" height="4" fill="var(--ember)"/>
      <text class="contact-text" x="203" y="45">Latchford St, Bromley</text>
    </g>
    <circle cx="152" cy="270" r="70" fill="var(--ember)" opacity="0.08"/>
    <path d="M0 395 Q150 360 305 392 L305 432 L0 432 Z" fill="var(--ember)"/>
    <path d="M0 405 Q160 380 305 410 L305 432 L0 432 Z" fill="var(--charcoal)"/>
    <text class="piece-label" x="110" y="446">Letter Head Option 1</text>
  </svg>

  <!-- Letterhead option 2 -->
  <svg class="letterhead-option-two" style="left:485px;top:12px" width="305" height="450" viewBox="0 0 305 450">
    <rect width="305" height="432" fill="var(--paper)"/>
    <path d="M0 0 L305 0 L305 6 Q150 -2 0 34 Z" fill="var(--charcoal)"/>
    <path d="M0 34 Q150 -2 305 6 L305 12 Q150 6 0 40 Z" fill="var(--ember)"/>
    <circle cx="108" cy="62" r="7" fill="var(--ember)"/>
    <text class="brand-name" x="120" y="63" font-size="10">CORAL VANTAGE LTD</text>
    <text class="tagline" x="120" y="70" font-size="4.5">GLOBAL STOCK SOLUTIONS</text>
    <circle cx="152" cy="280" r="70" fill="var(--ember)" opacity="0.08"/>
    <g class="footer-contacts">
      <rect x="50" y="404" width="4" height="4" fill="var(--ember)"/>
      <text class="contact-text" x="57" y="408">+44 20 7946 0321</text>
      <rect x="110" y="404" width="4" height="4" fill="var(--ember)"/>
      <text class="contact-text" x="117" y="408">Milo.harrigan@coralvantage.com</text>
      <rect x="202" y="404" width="4" height="4" fill="var(--ember)"/>
      <text class="contact-text" x="209" y="408">www.coralvantage.com</text>
    </g>
    <path d="M0 420 Q150 408 305 426 L305 432 L0 432 Z" fill="var(--ember)"/>
    <text class="piece-label" x="110" y="446">Letter Head Option 2</text>
  </svg>

  <!-- Envelope set -->
  <svg class="envelope-option-one" style="left:830px;top:12px" width="350" height="450" viewBox="0 0 350 450">
    <!-- envelope back, dark -->
    <rect x="0" y="0" width="350" height="135" fill="var(--coal)"/>
    <path d="M0 0 L175 95 L350 0 Z" fill="#333335"/>
    <circle cx="175" cy="78" r="6" fill="var(--ember)"/>

    <!-- envelope back, white with flap -->
    <rect x="0" y="128" width="350" height="100" fill="var(--paper)"/>
    <path d="M0 128 L350 128 L350 140 Q175 128 0 150 Z" fill="var(--ember)"/>
    <path d="M0 128 L175 200 L350 128" fill="none" stroke="#e8e8e8" stroke-width="1"/>
    <path d="M0 228 L175 175 L350 228" fill="none" stroke="#ececec" stroke-width="1"/>
    <circle cx="175" cy="165" r="5" fill="var(--ember)"/>

    <!-- envelope front -->
    <rect x="0" y="258" width="350" height="95" fill="var(--paper)"/>
    <circle cx="20" cy="276" r="6" fill="var(--ember)"/>
    <text class="brand-name" x="30" y="277" font-size="9">CORAL VANTAGE LTD</text>
    <text class="tagline" x="30" y="283" font-size="4">GLOBAL STOCK SOLUTIONS</text>
    <path d="M0 340 Q175 325 350 342 L350 353 L0 353 Z" fill="var(--ember)"/>

    <!-- envelope front, swoosh -->
    <rect x="0" y="360" width="350" height="75" fill="var(--paper)"/>
    <path d="M0 360 L350 360 L350 372 Q180 360 0 395 Z" fill="var(--charcoal)"/>
    <path d="M0 395 Q180 360 350 372 L350 378 Q180 368 0 402 Z" fill="var(--ember)"/>
    <text class="piece-label" x="130" y="446">Envelope Option 1</text>
  </svg>

</main>
</body>
</html>
```